Business Card Design Project

Company name will be Tolvan Crest (named after my black lab and his fraying muzzle) Business is in the body armor, Security product industry servicing the state, local, and federal law enforcement markets. I want a more formal and serious logo for both business cards and letterhead

```html
<!DOCTYPE html>
<html lang="en">
<head>
<meta charset="utf-8">
<title>Tolvan Crest — Business Card</title>
<link href="https://fonts.googleapis.com/css2?family=Marcellus&family=Tinos&display=swap" rel="stylesheet">
<style>
  :root {
    --page: #ffffff;
    --card: #0b0b0b;
    --card-glow: #1e1e1e;
    --frame-light: #6a6a6a;
    --frame-dark: #1a1a1a;
    --gold: #d9a22c;
    --mark-fill: #3a3a3c;
    --name: #bdbdbd;
    --contact: #f2f2f2;
  }
  html, body {
    margin: 0;
    padding: 0;
    width: 1200px;
    height: 998px;
    overflow: hidden;
    background: var(--page);
  }
  .canvas {
    position: relative;
    width: 1200px;
    height: 998px;
  }
  .card {
    position: absolute;
    left: 100px;
    top: 228px;
    width: 1000px;
    height: 541px;
    overflow: hidden;
    background: radial-gradient(ellipse at 42% 22%, var(--card-glow) 0%, var(--card) 60%);
  }
  .card-frame {
    position: absolute;
    left: 37px;
    top: 37px;
    width: 926px;
    height: 467px;
    box-sizing: border-box;
    border: 14px solid;
    border-color: var(--frame-light) var(--frame-dark) var(--frame-dark) var(--frame-light);
    border-image: linear-gradient(135deg, #7a7a7a, #2a2a2a 40%, #5c5c5c 70%, #1c1c1c) 1;
    box-shadow: inset 0 0 6px rgba(0,0,0,0.9), 0 0 4px rgba(0,0,0,0.8);
  }
  .brand-square {
    position: absolute;
    left: 99px;
    top: 94px;
    width: 168px;
    height: 192px;
    box-sizing: border-box;
    border: 10px solid var(--gold);
    background: var(--mark-fill);
  }
  .brand-name {
    position: absolute;
    left: 284px;
    top: 164px;
    margin: 0;
    font-family: "Marcellus", serif;
    font-weight: 400;
    font-size: 64px;
    line-height: 1;
    color: var(--name);
    white-space: nowrap;
  }
  .contact {
    position: absolute;
    left: 568px;
    top: 372px;
    margin: 0;
    padding: 0;
    list-style: none;
    font-family: "Tinos", serif;
    font-size: 21px;
    line-height: 27px;
    letter-spacing: 0.6px;
    color: var(--contact);
  }
  .contact li {
    margin: 0;
    white-space: pre;
  }
</style>
</head>
<body>
<main class="canvas">
  <section class="card" aria-label="Tolvan Crest business card">
    <div class="card-frame"></div>
    <div class="brand-square" aria-hidden="true"></div>
    <h1 class="brand-name">Tolvan Crest</h1>
    <ul class="contact">
      <li>adrees : Tolvan Crest place</li>
      <li>mobile : +00-0000000</li>
      <li>e-mail  : tolvan_crest@tc.com</li>
    </ul>
  </section>
</main>
</body>
</html>
```